Thornwell Consulting Cover 3 - Capital Allocation battlefield

Thornwell Consulting is a business consulting firm. We will publish a series of four thought leadership pieces online and via PDF. The third of the series is attached to this project. We need an eye-catching cover page with a back page that keeps with our branding. The document attached is in the final draft, and the cover and pack pages are placeholders only. You can find more about our branding and style on our website www.thornwellconsulting.com.au. The other three projects can be found here with a similar brief, and you are welcome to submit a design for all 4.

```html
<!DOCTYPE html>
<html lang="en">
<head>
<meta charset="utf-8">
<title>Thornwell Consulting – The Capital Allocation Battlefield</title>
<link rel="stylesheet" href="https://fonts.googleapis.com/css2?family=Poppins:wght@400;500;600;700&display=swap">
<style>
  :root {
    --stage: #5a5a5a;
    --label: #f2f2f2;
    --brand-blue: #0a7fcb;
    --deep-blue: #0461b0;
    --top-blue: #2aa8e8;
    --sky-blue: #35a9e6;
    --name-blue: #2aa3e0;
    --pale-blue: #9fd6f4;
    --brand-orange: #f39322;
    --paper: #f6f6f6;
    --white: #ffffff;
    --ink: #1d1d1f;
  }
  * { margin: 0; padding: 0; box-sizing: border-box; }
  html, body {
    width: 844px; height: 1200px; overflow: hidden;
    background: var(--stage);
    font-family: "Poppins", sans-serif;
  }
  .spread { position: relative; width: 844px; height: 1200px; }
  .page-label {
    position: absolute; top: 292px; width: 392px; text-align: center;
    color: var(--label); font-weight: 500; font-size: 16px;
  }
  .label-back { left: 20px; }
  .label-front { left: 432px; }
  .sheet {
    position: absolute; top: 330px; width: 392px; height: 544px; overflow: hidden;
    box-shadow: 0 6px 14px rgba(0,0,0,0.35);
  }
  .sheet-back { left: 20px; }
  .sheet-front { left: 432px; }
  .page {
    position: absolute; left: 0; top: 0; width: 720px; height: 1000px;
    transform: scale(0.5444); transform-origin: 0 0; overflow: hidden;
  }
  .page-art { position: absolute; inset: 0; width: 720px; height: 1000px; }

  /* Back page */
  .back { background: var(--white); }
  .back-brand {
    position: absolute; left: 190px; top: 88px;
    display: flex; align-items: center; gap: 10px;
  }
  .back-brand .brand-dot { width: 40px; height: 40px; border-radius: 50%; background: var(--brand-orange); }
  .back-brand .brand-name { color: var(--white); font-weight: 600; font-size: 20px; line-height: 1.0; }
  .back-pitch {
    position: absolute; left: 190px; top: 155px; width: 460px;
    color: var(--white); font-size: 16px; line-height: 22px;
  }
  .back-pitch .accent { color: var(--brand-orange); font-weight: 600; }
  .follow {
    position: absolute; right: 110px; top: 242px;
    display: flex; align-items: center; gap: 8px;
    color: var(--white); font-size: 13px;
  }
  .follow .social { width: 15px; height: 15px; border-radius: 3px; background: var(--white); }
  .contact { position: absolute; top: 836px; }
  .contact-left { left: 52px; }
  .contact-right { left: 412px; }
  .contact-name { color: var(--name-blue); font-weight: 600; font-size: 20px; line-height: 24px; }
  .contact-role { color: var(--brand-orange); font-size: 15px; line-height: 18px; }
  .contact-line {
    display: flex; align-items: center; gap: 14px; color: var(--ink);
  }
  .contact-phone { margin-top: 18px; font-size: 17px; line-height: 24px; }
  .contact-email { font-size: 13.5px; line-height: 22px; }
  .contact-line svg { width: 15px; height: 15px; flex: none; }

  /* Front page */
  .front { background: var(--paper); }
  .front-brand {
    position: absolute; left: 52px; top: 84px;
    display: flex; align-items: center; gap: 14px;
  }
  .front-brand .brand-dot { width: 58px; height: 58px; border-radius: 50%; background: var(--brand-orange); }
  .front-brand .brand-name { color: var(--brand-blue); font-weight: 600; font-size: 34px; line-height: 1.0; }
  .title {
    position: absolute; left: 50px; top: 520px;
    color: var(--white); font-weight: 600; font-size: 58px; line-height: 68px; letter-spacing: -0.3px;
  }
  .subtitle {
    position: absolute; left: 55px; top: 750px;
    padding-left: 12px; border-left: 4px solid var(--brand-orange);
    color: var(--white); font-weight: 600; font-size: 18.5px; line-height: 28px;
  }
  .web-address {
    position: absolute; right: 52px; top: 882px;
    color: var(--white); font-size: 16px;
  }
</style>
</head>
<body>
<div class="spread">
  <p class="page-label label-back">Back</p>
  <p class="page-label label-front">Front</p>

  <section class="sheet sheet-back">
    <div class="page back">
      <svg class="page-art" viewBox="0 0 720 1000" xmlns="http://www.w3.org/2000/svg">
        <defs>
          <linearGradient id="back-sky" x1="0" y1="0" x2="0" y2="1">
            <stop offset="0" stop-color="#2aa8e8"/>
            <stop offset="0.35" stop-color="#0a7fcb"/>
            <stop offset="1" stop-color="#0461b0"/>
          </linearGradient>
          <linearGradient id="skyline-tone" x1="0" y1="0" x2="0" y2="1">
            <stop offset="0" stop-color="#e3eef8"/>
            <stop offset="0.55" stop-color="#8fb8dc"/>
            <stop offset="1" stop-color="#d9e6ee"/>
          </linearGradient>
          <linearGradient id="fade-blue" x1="0" y1="0" x2="0" y2="1">
            <stop offset="0" stop-color="#bfe0f5" stop-opacity="0.8"/>
            <stop offset="1" stop-color="#ffffff" stop-opacity="0"/>
          </linearGradient>
        </defs>
        <rect x="0" y="0" width="720" height="520" fill="url(#back-sky)"/>
        <circle cx="400" cy="820" r="470" fill="var(--white)"/>
        <ellipse cx="300" cy="1010" rx="330" ry="250" fill="url(#fade-blue)"/>
        <circle class="skyline-photo" role="img" aria-label="Photo of glass office towers under a cloudy sky"
                cx="344" cy="584" r="222" fill="url(#skyline-tone)"/>
        <circle cx="620" cy="660" r="215" fill="#5fc6f2" opacity="0.85"/>
        <circle cx="660" cy="660" r="190" fill="#0a94d8" opacity="0.85"/>
        <circle cx="700" cy="680" r="150" fill="#0a7fcb" opacity="0.8"/>
        <rect x="0" y="780" width="720" height="220" fill="var(--white)" opacity="0.55"/>
      </svg>

      <div class="back-brand">
        <span class="brand-dot"></span>
        <span class="brand-name">Thornwell<br>Consulting</span>
      </div>
      <p class="back-pitch">Contact us to find out how <span class="accent">Thornwell Consulting</span> can help build your company into a market leader today.</p>
      <div class="follow">
        <span>Follow us:</span>
        <span class="social"></span>
        <span class="social"></span>
      </div>

      <div class="contact contact-left">
        <p class="contact-name">Edward Thornwell</p>
        <p class="contact-role">Managing Director</p>
        <p class="contact-line contact-phone">
          <svg viewBox="0 0 16 16"><path d="M4 1.5 6.2 4 5 5.6c.8 1.9 2.4 3.5 4.4 4.4L11 8.8l2.5 2.2-1.3 2.4C7 13 3 9 2.6 3.8Z" fill="var(--brand-orange)"/></svg>
          +61 400 318 205
        </p>
        <p class="contact-line contact-email">
          <svg viewBox="0 0 16 16"><rect x="1" y="3.5" width="14" height="9" rx="1" fill="var(--brand-orange)"/><path d="M1.5 4 8 9l6.5-5" stroke="#fff" stroke-width="1.2" fill="none"/></svg>
          edward@thornwellconsulting.com.au
        </p>
      </div>
      <div class="contact contact-right">
        <p class="contact-name">Oliver Thornwell</p>
        <p class="contact-role">Managing Director</p>
        <p class="contact-line contact-phone">
          <svg viewBox="0 0 16 16"><path d="M4 1.5 6.2 4 5 5.6c.8 1.9 2.4 3.5 4.4 4.4L11 8.8l2.5 2.2-1.3 2.4C7 13 3 9 2.6 3.8Z" fill="var(--brand-orange)"/></svg>
          +61 400 726 914
        </p>
        <p class="contact-line contact-email">
          <svg viewBox="0 0 16 16"><rect x="1" y="3.5" width="14" height="9" rx="1" fill="var(--brand-orange)"/><path d="M1.5 4 8 9l6.5-5" stroke="#fff" stroke-width="1.2" fill="none"/></svg>
          oliver@thornwellconsulting.com.au
        </p>
      </div>
    </div>
  </section>

  <section class="sheet sheet-front">
    <div class="page front">
      <svg class="page-art" viewBox="0 0 720 1000" xmlns="http://www.w3.org/2000/svg">
        <defs>
          <linearGradient id="tower-tone" x1="1" y1="0" x2="0" y2="1">
            <stop offset="0" stop-color="#e4e4e4"/>
            <stop offset="0.6" stop-color="#efefef"/>
            <stop offset="1" stop-color="#f7f7f7"/>
          </linearGradient>
          <linearGradient id="city-tone" x1="0" y1="0" x2="0" y2="1">
            <stop offset="0" stop-color="#1b8fd6"/>
            <stop offset="1" stop-color="#0357a6"/>
          </linearGradient>
          <radialGradient id="glass-circle" cx="0.5" cy="0.45" r="0.6">
            <stop offset="0" stop-color="#6cbcec" stop-opacity="0.85"/>
            <stop offset="1" stop-color="#1f95dc" stop-opacity="0.95"/>
          </radialGradient>
        </defs>
        <rect class="tower-photo" role="img" aria-label="Photo of a white curved office tower seen from below"
              x="200" y="0" width="520" height="600" fill="url(#tower-tone)"/>
        <circle cx="400" cy="800" r="520" fill="var(--white)" opacity="0.9"/>
        <rect class="city-photo" role="img" aria-label="Blue-tinted photo of a city skyline with glass towers"
              x="0" y="640" width="720" height="360" fill="url(#city-tone)"/>
        <circle class="circle-photo" role="img" aria-label="Blue-tinted photo of glass skyscrapers in a circle"
                cx="600" cy="690" r="300" fill="url(#glass-circle)"/>
        <circle cx="600" cy="690" r="300" fill="none" stroke="var(--pale-blue)" stroke-width="34" opacity="0.5"/>
        <circle class="title-disc" cx="110" cy="665" r="310" fill="var(--brand-blue)"/>
        <rect x="0" y="850" width="720" height="150" fill="var(--deep-blue)" opacity="0.5"/>
      </svg>

      <div class="front-brand">
        <span class="brand-dot"></span>
        <span class="brand-name">Thornwell<br>Consulting</span>
      </div>
      <h1 class="title">The Capital<br>Allocation<br>Battlefield</h1>
      <p class="subtitle">Deploying the War Chest</p>
      <p class="web-address">thornwellconsulting.com.au</p>
    </div>
  </section>
</div>
</body>
</html>
```